Marketing & Media Production Company wants edgy DESIGN + CODING

Please find enclosed in the Brief document
we really want this website to be edgy, monochrome (ie. only two colors - white + black) with some nice background imagery STRICTLY based on the logo.
The logo is a sumerian eagle, it would be great to keep this as a subtle background theme but dont go crazy on this.
Please feel free to ignore the layout in the document if you think you can come up with one that is better, ideally we want the layout to be CLEAR and easy to decipher - with a really good contact form on the front page.
We want the website to be cool, funky, so if you want to have a introductory picture that must be clicked (logo) or something like that (eg this website:
Please NOTE:
Page Structure is as follows:
1 ABOUT US > (subpage) Meet the Team
2 CLIENTS > (subpage) Case Studies
3 SERVICES > (subpage) Portfolio
4 CONTACT
Industry/Entity Type
It Company

```html
<!DOCTYPE html>
<html lang="en">
<head>
<meta charset="utf-8">
<title>Vantage — Marketing &amp; Media Production</title>
<link rel="stylesheet" href="https://fonts.googleapis.com/css2?family=Josefin+Sans:wght@400;600&family=Open+Sans:ital,wght@0,400;0,600;1,400&display=swap">
<style>
  :root {
    --ink: #0b0b0b;
    --paper: #ffffff;
    --nav-ink: #1c1c1c;
    --panel: rgba(74, 74, 74, 0.82);
    --panel-solid: #464646;
    --panel-line: rgba(255, 255, 255, 0.85);
    --field: #767676;
    --field-line: rgba(255, 255, 255, 0.75);
    --rule: rgba(255, 255, 255, 0.25);
    --chip-top: #ffffff;
    --chip-bottom: #c9c9c9;
  }
  * { box-sizing: border-box; margin: 0; padding: 0; }
  html, body { width: 1200px; height: 1051px; overflow: hidden; background: var(--ink); }
  body { position: relative; font-family: "Open Sans", sans-serif; color: var(--paper); }

  .hero-backdrop {
    position: absolute; left: 0; top: 0; width: 1200px; height: 482px;
    background: linear-gradient(180deg, #f4f4f4 0%, #e2e2e2 25%, #bdbdbd 45%, #7a7a7a 65%, #3a3a3a 85%, var(--ink) 100%);
  }

  .main-nav a {
    position: absolute; top: 78px; font-size: 16px; letter-spacing: 0.5px;
    color: var(--nav-ink); text-decoration: none; font-family: "Open Sans", sans-serif;
  }
  .nav-about { left: 132px; } .nav-clients { left: 322px; }
  .nav-services { left: 790px; } .nav-contact { left: 972px; }

  .brand {
    position: absolute; left: 500px; top: 70px; width: 200px; text-align: center;
    font-family: "Josefin Sans", sans-serif; font-weight: 600; font-size: 26px;
    letter-spacing: 8px; color: var(--nav-ink);
  }
  .brand-dot {
    display: block; width: 36px; height: 36px; border-radius: 50%;
    background: var(--nav-ink); margin: -44px auto 12px;
  }

  .panel {
    position: absolute; background: var(--panel);
    border: 1px solid var(--panel-line); border-radius: 5px;
  }
  .panel-title {
    position: absolute; font-family: "Josefin Sans", sans-serif; font-weight: 400;
    font-size: 23px; letter-spacing: 1px; color: var(--paper);
  }
  .view-more {
    position: absolute; font-size: 11px; font-style: italic;
    color: var(--paper); text-decoration: underline;
  }

  .services { left: 88px; top: 317px; width: 506px; height: 251px; }
  .services .panel-title { left: 37px; top: 25px; }
  .services .view-more { right: 31px; top: 29px; }
  .service-item { position: absolute; font-size: 16.5px; white-space: nowrap; }
  .service-item::before { content: "»"; margin-right: 4px; }

  .news { left: 606px; top: 317px; width: 507px; height: 251px; }
  .news .panel-title { left: 28px; top: 25px; }
  .news .view-more { right: 28px; top: 28px; }
  .news-item { position: absolute; left: 28px; width: 460px; height: 56px; }
  .news-date {
    position: absolute; left: 0; top: 0; width: 60px; height: 55px; border-radius: 6px;
    background: linear-gradient(180deg, var(--chip-top), var(--chip-bottom));
    color: var(--ink); text-align: center; font-size: 15px; line-height: 21px; padding-top: 6px;
  }
  .news-headline { position: absolute; left: 70px; top: 0; font-size: 12.5px; font-weight: 600; letter-spacing: 0.3px; white-space: nowrap; }
  .news-excerpt { position: absolute; left: 70px; top: 17px; font-size: 11.5px; line-height: 19px; width: 400px; }
  .news-rule { position: absolute; left: 31px; top: 143px; width: 446px; height: 1px; background: var(--rule); }

  .contact { left: 88px; top: 586px; width: 1025px; height: 375px; background: var(--panel-solid); }
  .contact .panel-title { left: 0; width: 1025px; text-align: center; top: 24px; }
  .field {
    position: absolute; background: var(--field); border: 1px solid var(--field-line);
    border-radius: 8px; box-shadow: inset 0 8px 8px -4px rgba(0,0,0,0.35);
    color: var(--paper); font-size: 15px; letter-spacing: 0.4px; padding: 20px 18px;
  }
  .field-name { left: 64px; top: 78px; width: 288px; height: 60px; }
  .field-email { left: 376px; top: 78px; width: 289px; height: 60px; }
  .field-phone { left: 689px; top: 78px; width: 289px; height: 60px; }
  .field-message { left: 64px; top: 163px; width: 914px; height: 91px; padding-top: 18px; }
  .submit-button {
    position: absolute; left: 64px; top: 273px; width: 143px; height: 49px; border-radius: 3px;
    background: linear-gradient(180deg, #ffffff, #c4c4c4); color: var(--ink);
    font-size: 16px; font-weight: 600; letter-spacing: 1px; text-align: center; line-height: 49px;
  }
  .contact-note { position: absolute; left: 240px; top: 290px; font-size: 13px; letter-spacing: 0.3px; }

  .footer-brand {
    position: absolute; left: 88px; top: 997px; font-family: "Josefin Sans", sans-serif;
    font-weight: 600; font-size: 16px; letter-spacing: 4px; color: var(--paper);
  }
  .social-link {
    position: absolute; top: 993px; width: 26px; height: 26px; border-radius: 50%;
    background: linear-gradient(180deg, #f0f0f0, #9a9a9a);
  }
  .copyright { position: absolute; right: 100px; top: 998px; font-size: 12.5px; }
</style>
</head>
<body>
  <div class="hero-backdrop" role="img" aria-label="Misty monochrome mountain range fading into black"></div>

  <nav class="main-nav">
    <a class="nav-about" href="#">ABOUT US</a>
    <a class="nav-clients" href="#">CLIENTS</a>
    <a class="nav-services" href="#">SERVICES</a>
    <a class="nav-contact" href="#">CONTACT US</a>
  </nav>

  <div class="brand"><span class="brand-dot"></span>VANTAGE</div>

  <section class="panel services">
    <h2 class="panel-title">SERVICES</h2>
    <a class="view-more" href="#">View more</a>
    <div class="service-item" style="left:39px;top:87px">Media production</div>
    <div class="service-item" style="left:264px;top:88px">Simply dummy text</div>
    <div class="service-item" style="left:39px;top:137px">Digital marketing</div>
    <div class="service-item" style="left:262px;top:137px">Ipsum is simply dummy</div>
    <div class="service-item" style="left:40px;top:185px">Branding consultancy</div>
    <div class="service-item" style="left:262px;top:185px">simply dummy text</div>
  </section>

  <section class="panel news">
    <h2 class="panel-title">LATEST NEWS</h2>
    <a class="view-more" href="#">View more</a>
    <article class="news-item" style="top:71px">
      <div class="news-date">26<br>JAN</div>
      <h3 class="news-headline">LOREM IPSUM IS SIMPLY DUMMY TEXT</h3>
      <p class="news-excerpt">Lorem Ipsum has been the industry's standard dummy text ever since the 1500s, when an unknown printer took a galley scrambled</p>
    </article>
    <div class="news-rule"></div>
    <article class="news-item" style="top:159px">
      <div class="news-date">27<br>JAN</div>
      <h3 class="news-headline">LOREM IPSUM IS SIMPLY DUMMY TEXT</h3>
      <p class="news-excerpt">Lorem Ipsum has been the industry's standard dummy text ever since the 1500s, when an unknown printer took a galley scrambled</p>
    </article>
  </section>

  <section class="panel contact">
    <h2 class="panel-title">CONTACT FORM</h2>
    <div class="field field-name">Name :</div>
    <div class="field field-email">Email ID :</div>
    <div class="field field-phone">Phone :</div>
    <div class="field field-message">Massage :</div>
    <div class="submit-button">SUBMIT</div>
    <p class="contact-note">Lorem Ipsum has been the industry's standard dummy text ever since the 1500s, when an unknown printer</p>
  </section>

  <footer>
    <div class="footer-brand">VANTAGE</div>
    <a class="social-link" href="#" aria-label="Social link" style="left:541px"></a>
    <a class="social-link" href="#" aria-label="Social link" style="left:583px"></a>
    <a class="social-link" href="#" aria-label="Social link" style="left:625px"></a>
    <p class="copyright">Copyright © 2015&nbsp; All Rights Reserved</p>
  </footer>
</body>
</html>
```